Velmora Strom GmbH webpage The online Business card of a master electrician

A clean, modern webpage on whitch i can show my clients what im capable of and where the future costumer can inform himself. I need a login page for costumers who are registred and an secound webpage where my stuff can login to report theyr labour.
I will post pictures before and after, put on some commercial and crossellimg informations.
The costumer should find my insta as well my twitter or snapchat accounts.

Update:
Our Services are, Installations, Renovations, Home Automation, CCTV, Telefon / VOIP, Networking / Network-Cabeling, Electrical Supervisioning

Target Market(s)

Private and business costumers

Industry/Entity Type

Electric Company

Number of Pages Required

5+ page

Font styles to use
Sans Serif
Other font styles liked:
• Zurich,

Colors

Designer to choose colors to be used in the design.

Requirements
Must have
• A Page Hero
• A Costumer and staff login page (2separate pages)
• Contact form
• Responsive form
• Instagram enbedding account velmora_strom
Nice to have
• A Blog

```html
<!DOCTYPE html>
<html lang="en">
<head>
<meta charset="utf-8">
<title>Velmora Strom GmbH</title>
<link href="https://fonts.googleapis.com/css2?family=Open+Sans:wght@300;400;600;700&display=swap" rel="stylesheet">
<style>
:root{
  --brand:#1a4a9c;
  --brand-light:#2d63c4;
  --text:#666;
  --nav:#777;
  --soft-bg:#f7f7f7;
  --white:#fff;
  --accent:#8cc63f;
}
*{margin:0;padding:0;box-sizing:border-box}
html,body{width:1198px;height:1200px;overflow:hidden;background:var(--white);font-family:"Open Sans",sans-serif}
.page{position:relative;width:1198px;height:1200px}
.topbar{position:absolute;left:0;top:0;width:100%;height:30px;background:var(--brand);color:var(--white);font-size:14px}
.topbar .mail{position:absolute;left:114px;top:5px;display:flex;align-items:center;gap:7px}
.topbar .phone{position:absolute;right:109px;top:5px;display:flex;align-items:center;gap:7px;font-size:15px}
.header{position:absolute;top:30px;left:0;width:100%;height:66px;background:var(--white);border-bottom:1px solid #eee}
.brand{position:absolute;left:106px;top:22px;display:flex;align-items:center;gap:8px;font-weight:700;font-size:19px;color:var(--brand)}
.brand .mark{width:14px;height:14px;background:var(--brand)}
.nav{position:absolute;top:23px;left:0;font-size:12px;color:var(--nav);text-transform:uppercase}
.nav a{position:absolute;white-space:nowrap;text-decoration:none;color:var(--nav)}
.nav a.active{color:var(--brand);font-weight:700}
.nav a.active::after{content:"";position:absolute;left:-7px;right:-9px;top:29px;height:3px;background:var(--brand)}
.hero{position:absolute;top:96px;left:0;width:100%;height:521px;background:linear-gradient(100deg,#4b4f57 0%,#8a8d92 40%,#b9bbbe 70%,#8c8e90 100%);color:var(--white);text-align:center}
.hero::before{content:"";position:absolute;inset:0;background:rgba(40,40,45,.25)}
.hero h1{position:relative;padding-top:195px;font-size:43px;font-weight:300;text-shadow:0 2px 6px rgba(0,0,0,.4)}
.hero h1 strong{font-weight:700}
.hero p{position:relative;margin:10px auto 0;width:740px;font-size:17px;line-height:30px;text-shadow:0 1px 4px rgba(0,0,0,.5)}
.dots{position:absolute;left:585px;top:446px;display:flex;align-items:center;gap:2px}
.dots span{width:5px;height:5px;border-radius:50%;background:#ccc}
.dots span.on{width:9px;height:9px;background:var(--accent)}
.about{position:absolute;top:617px;left:0;width:100%;height:304px;text-align:center}
.section-title{font-size:32px;font-weight:400;color:var(--brand-light)}
.section-title strong{font-weight:700;color:var(--brand)}
.about .section-title{margin-top:40px}
.about p{width:880px;margin:14px auto 0;font-size:15px;line-height:23.3px;color:var(--text);font-weight:300}
.about p + p{margin-top:23px}
.services{position:absolute;top:921px;left:0;width:100%;height:279px;background:var(--soft-bg)}
.services .section-title{text-align:center;margin-top:34px}
.service{position:absolute;top:128px;width:440px}
.service .icon{position:absolute;left:0;top:0;width:52px;height:52px;border-radius:50%;background:var(--brand-light);display:flex;align-items:center;justify-content:center}
.service h3{margin-left:62px;font-size:17.5px;line-height:24px;font-weight:400;color:#555;padding-top:0}
.service p{margin-top:10px;margin-left:3px;font-size:12.5px;line-height:21.6px;color:#aaa;letter-spacing:.2px}
.service.alt .icon{background:var(--brand)}
.service.alt h3{color:var(--brand-light)}
.service.alt p{color:#555}
</style>
</head>
<body>
<div class="page">
  <div class="topbar">
    <div class="mail">
      <svg width="16" height="11" viewBox="0 0 16 11"><rect x="0.5" y="0.5" width="15" height="10" fill="#fff"/><path d="M1 1l7 5 7-5" stroke="#1a4a9c" stroke-width="1.3" fill="none"/></svg>
      info@velmorastrom.co.uk
    </div>
    <div class="phone">
      <svg width="18" height="14" viewBox="0 0 18 14"><path d="M1 5c0-3 16-3 16 0v1h-4V4H5v2H1z" fill="#fff"/><path d="M4 7h10l2 6H2z" fill="#fff"/><circle cx="9" cy="10" r="1.6" fill="#1a4a9c"/></svg>
      +8 55 555 5555
    </div>
  </div>

  <header class="header">
    <div class="brand"><span class="mark"></span>Velmora Strom</div>
    <nav class="nav">
      <a class="active" style="left:359px">Home</a>
      <a style="left:443px">Installation</a>
      <a style="left:572px">Maintenance</a>
      <a style="left:703px">Home Automation</a>
      <a style="left:868px">Network-Cabeling</a>
      <a style="left:1031px">Contact</a>
    </nav>
  </header>

  <section class="hero" role="img" aria-label="Photo of an electrician servicing a wall-mounted air conditioning unit">
    <h1>Welcom To <strong>VELMORA STROM</strong></h1>
    <p>It is a long established fact that a reader will be distracted by the readable content of a page when looking at its layout.</p>
    <div class="dots"><span></span><span class="on"></span><span></span><span style="width:4px;height:4px"></span></div>
  </section>

  <section class="about">
    <h2 class="section-title">About <strong>VELMORA STROM</strong></h2>
    <p>It is a long established fact that a reader will be distracted by the readable content of a page when looking at its layout. The point of using Lorem Ipsum is that it has a more-or-less normal distribution of letters, as opposed to using 'Content here, content here', making it look like readable English.</p>
    <p>Many desktop publishing packages and web page editors now use Lorem Ipsum as their default model text, and a search for 'lorem ipsum' will uncover many web sites still in their infancy. Various versions have evolved over the years, sometimes by accident, sometimes on purpose (injected humour and the like).</p>
  </section>

  <section class="services">
    <h2 class="section-title">Our <strong>SERVICES</strong></h2>
    <div class="service" style="left:112px">
      <div class="icon">
        <svg width="28" height="28" viewBox="0 0 28 28"><g stroke="#fff" stroke-width="5" stroke-linecap="round"><path d="M14 3v22"/><path d="M4.5 8.5l19 11"/><path d="M4.5 19.5l19-11"/></g></svg>
      </div>
      <h3>We’ll easily cope with planning of conditioning and ventilation</h3>
      <p>Our specialists are ready to perform the planning of conditioning and ventilation sections of such objects as business centers, hypermarkets, hotels, shopping, exhibitions and  industrial buildings.</p>
    </div>
    <div class="service alt" style="left:596px">
      <div class="icon">
        <svg width="28" height="28" viewBox="0 0 28 28"><path d="M5 23L15 13" stroke="#fff" stroke-width="4.5" stroke-linecap="round"/><path d="M14 10a6 6 0 0 1 9-6l-4 4 1 3 3 1 4-4a6 6 0 0 1-8 8z" fill="#fff"/><circle cx="6.5" cy="21.5" r="1" fill="#1a4a9c"/></svg>
      </div>
      <h3>You can be sure in our maintenance and support 24/7</h3>
      <p>Our specialists are ready to perform the planning of conditioning and ventilation sections of such objects as business centers, hypermarkets, hotels, shopping, exhibitions and  industrial buildings.</p>
    </div>
  </section>
</div>
</body>
</html>
```